Awesome Pavement Maintenance Company Needs New Postcard!

We are an Asphalt Maintenance contractor in need of a new Postcard design for our Fall direct mail campaign. Our services include Crack Filling, Sealcoating, Line Striping and Asphalt Patching. Fall is a busy time of year for Parking Lot Maintenance services in Connecticut, USA where we are located, and we need to capture as much business from this mail piece as we possibly can. People enlist our services in preparation for winter so the winning design will have a call to action that we think has the best chance of getting our phone to ring. Come up with a new look and feel for us in your design.

Feel free to use our images attached, or stock images. An example of one of our current cards is attached also. PLEASE: use the template provided for layout specifications.

Target Market(s)

Commercial/Industrial Facility Managers, Condo/Apartment Building Property Managers, Owners of Commercial Real Estate, Business Owners, etc.

Industry/Entity Type

Construction Company

Requirements
Must have
• A Call to Action
• Our Phone Number: 860-417-2938
• Our website: www.brinweldpavement.example
Nice to have
• Our 4 Main Services Listed
• -Asphalt Patching
• - Crack Filling
• -Sealcoating
• -Line Striping
• Photos? We have plenty or use stock
Should not have
• Misspelling of our name. Should be BrinWELD -not 'coast'!

```html
<!DOCTYPE html>
<html lang="en">
<head>
<meta charset="utf-8">
<title>BrinWeld Pavement Services – Fall Postcard</title>
<link href="https://fonts.googleapis.com/css2?family=Montserrat:wght@700;800&family=Lato:ital,wght@0,400;0,700;0,900;1,400;1,700&display=swap" rel="stylesheet">
<style>
  :root{
    --red:#d42027;
    --red-dark:#a8151b;
    --asphalt:#1f1f1f;
    --asphalt-mid:#2e2e2e;
    --charcoal:#333335;
    --ink:#1a1a1a;
    --white:#ffffff;
    --paper:#ffffff;
    --quote-band:#d8d8d8;
    --page:#ececec;
    --line:#9a9a9a;
  }
  html,body{margin:0;padding:0;width:900px;height:1200px;overflow:hidden;background:var(--page);}
  .sheet{position:relative;width:900px;height:1200px;}
  .postcard{position:absolute;left:60px;width:780px;height:504px;display:block;box-shadow:0 2px 8px rgba(0,0,0,.18);}
  .postcard--front{top:60px;}
  .postcard--back{top:636px;}
  .headline{font-family:"Montserrat",sans-serif;font-weight:800;font-size:27px;letter-spacing:.5px;}
  .headline--dark{fill:var(--ink);}
  .headline--light{fill:var(--white);font-size:29px;}
  .brand-name{font-family:"Lato",sans-serif;font-weight:900;font-size:30px;fill:#3b3b3b;letter-spacing:-.5px;}
  .brand-tagline{font-family:"Lato",sans-serif;font-weight:900;font-size:10.5px;fill:var(--ink);letter-spacing:1px;}
  .pill-label{font-family:"Lato",sans-serif;font-weight:900;font-size:15px;fill:var(--white);}
  .pill-label--back{font-size:15px;}
  .service{font-family:"Lato",sans-serif;font-style:italic;font-weight:700;font-size:13.5px;fill:var(--white);}
  .quote{font-family:"Lato",sans-serif;font-style:italic;font-weight:700;font-size:7px;fill:var(--ink);}
  .quote-mark{font-family:"Lato",sans-serif;font-weight:900;font-size:14px;fill:var(--red);}
  .quote-author{font-family:"Lato",sans-serif;font-size:7px;fill:var(--red);}
  .website{font-family:"Lato",sans-serif;font-weight:700;font-size:13px;fill:var(--white);letter-spacing:.8px;}
  .cta-small{font-family:"Lato",sans-serif;font-weight:700;font-size:17px;fill:var(--white);}
  .phone{font-family:"Lato",sans-serif;font-weight:900;font-size:32px;fill:var(--white);letter-spacing:-.5px;}
  .cta-sub{font-family:"Lato",sans-serif;font-weight:700;font-size:16px;fill:var(--ink);}
  .follow{font-family:"Lato",sans-serif;font-weight:700;font-size:11px;fill:var(--white);}
  .about{font-family:"Lato",sans-serif;font-size:10.4px;fill:var(--white);}
  .cta-back{font-family:"Lato",sans-serif;font-weight:900;font-size:15px;fill:var(--red);}
  .phone--back{font-size:36px;}
</style>
</head>
<body>
<main class="sheet">

  <!-- Front side -->
  <svg class="postcard postcard--front" viewBox="0 0 703 454" xmlns="http://www.w3.org/2000/svg" aria-label="Postcard front">
    <defs>
      <linearGradient id="asphaltFill" x1="0" y1="0" x2="0" y2="1">
        <stop offset="0" stop-color="#2a2a2a"/><stop offset="1" stop-color="#171717"/>
      </linearGradient>
      <linearGradient id="lotPhoto" x1="0" y1="0" x2="0" y2="1">
        <stop offset="0" stop-color="#bcd2ea"/><stop offset=".28" stop-color="#d9dcde"/>
        <stop offset=".42" stop-color="#8c8f92"/><stop offset="1" stop-color="#5e6266"/>
      </linearGradient>
      <linearGradient id="aerialPhoto" x1="0" y1="0" x2="1" y2="1">
        <stop offset="0" stop-color="#7d9a5a"/><stop offset=".5" stop-color="#4d5a6c"/><stop offset="1" stop-color="#6f8a4c"/>
      </linearGradient>
      <linearGradient id="redPanel" x1="0" y1="0" x2="0" y2="1">
        <stop offset="0" stop-color="#e0262d"/><stop offset="1" stop-color="#c21c22"/>
      </linearGradient>
    </defs>

    <rect width="703" height="454" fill="url(#asphaltFill)"/>

    <!-- brand block -->
    <rect class="brand-block" x="0" y="0" width="420" height="92" fill="var(--paper)"/>
    <circle cx="40" cy="40" r="9" fill="var(--red)"/>
    <text class="brand-name" x="55" y="51">brinweld</text>
    <text class="brand-tagline" x="38" y="69">PAVEMENT SERVICES</text>

    <!-- headline banner -->
    <rect x="0" y="92" width="330" height="90" fill="url(#redPanel)"/>
    <text class="headline headline--dark" x="20" y="128">ARE YOU READY</text>
    <text class="headline headline--light" x="20" y="166">FOR WINTER?</text>

    <!-- photo area with swoosh edges -->
    <path d="M392,0 H703 V262 C600,272 500,300 430,350 C350,300 300,220 318,130 C328,70 355,25 392,0 Z" fill="var(--white)"/>
    <path d="M404,0 H703 V250 C600,260 505,288 436,334 C362,290 318,215 333,130 C342,75 368,28 404,0 Z" fill="var(--ink)"/>
    <path role="img" aria-label="Photo: crew member line-striping a fresh parking lot in front of condo buildings" d="M412,0 H703 V240 C600,250 508,278 440,322 C372,280 330,210 344,130 C352,78 378,30 412,0 Z" fill="url(#lotPhoto)"/>

    <!-- red call-to-action panel -->
    <path d="M268,454 C270,360 340,320 430,320 C540,318 620,285 703,255 V454 Z" fill="var(--white)"/>
    <path d="M282,454 C284,368 348,332 432,332 C540,330 622,298 703,270 V454 Z" fill="var(--ink)"/>
    <path d="M296,454 C298,376 356,342 434,342 C542,340 624,310 703,283 V454 Z" fill="url(#redPanel)"/>

    <!-- circular service photos -->
    <circle role="img" aria-label="Photo: aerial view of a freshly sealed parking lot" cx="377" cy="247" r="79" fill="url(#aerialPhoto)" stroke="var(--white)" stroke-width="4"/>
    <circle role="img" aria-label="Photo: aerial view of apartment complex parking" cx="500" cy="287" r="46" fill="url(#aerialPhoto)" stroke="var(--white)" stroke-width="4"/>
    <circle role="img" aria-label="Photo: aerial view of a striped lot beside a lawn" cx="604" cy="306" r="46" fill="url(#aerialPhoto)" stroke="var(--white)" stroke-width="4"/>

    <!-- services -->
    <path d="M0,197 H138 A12,12 0 0 1 138,221 H0" fill="none" stroke="var(--white)" stroke-width="1.5"/>
    <text class="pill-label" x="20" y="214">Our services</text>

    <g class="service-list">
      <g transform="translate(20,247)">
        <rect width="11" height="11" fill="var(--white)"/>
        <path d="M2,6 L5,9 L13,-1" fill="none" stroke="var(--red)" stroke-width="2.6" stroke-linecap="round"/>
      </g>
      <text class="service" x="45" y="258">Asphalt Patching</text>
      <g transform="translate(167,247)">
        <rect width="11" height="11" fill="var(--white)"/>
        <path d="M2,6 L5,9 L13,-1" fill="none" stroke="var(--red)" stroke-width="2.6" stroke-linecap="round"/>
      </g>
      <text class="service" x="187" y="258">Sealcoating</text>
      <g transform="translate(20,273)">
        <rect width="11" height="11" fill="var(--white)"/>
        <path d="M2,6 L5,9 L13,-1" fill="none" stroke="var(--red)" stroke-width="2.6" stroke-linecap="round"/>
      </g>
      <text class="service" x="45" y="284">Crack Filling</text>
      <g transform="translate(167,273)">
        <rect width="11" height="11" fill="var(--white)"/>
        <path d="M2,6 L5,9 L13,-1" fill="none" stroke="var(--red)" stroke-width="2.6" stroke-linecap="round"/>
      </g>
      <text class="service" x="187" y="284">Line Striping</text>
    </g>

    <!-- testimonial -->
    <path d="M0,322 H300 C292,345 288,370 290,393 H0 Z" fill="var(--quote-band)"/>
    <text class="quote-mark" x="12" y="341">“</text>
    <text class="quote" x="22" y="339">BrinWeld Pavement Services were true professionals that worked to</text>
    <text class="quote" x="22" y="348">accommodate our employee's schedule and our parking lots have not</text>
    <text class="quote" x="22" y="357">looked this good in years <tspan class="quote-mark" font-size="12">”</tspan></text>
    <text class="quote-author" x="22" y="372">DANA WHITLOCK</text>
    <text class="quote-author" x="22" y="381">HARLOW TOOL WORKS, A TOP 500 COMPANY</text>

    <!-- website -->
    <circle cx="28" cy="420" r="4" fill="none" stroke="var(--red)" stroke-width="1.5"/>
    <line x1="24" y1="420" x2="32" y2="420" stroke="var(--red)" stroke-width="1"/>
    <text class="website" x="40" y="424">www.brinweldpavement.example</text>

    <!-- call to action -->
    <text class="cta-small" x="336" y="375">CALL</text>
    <circle cx="311" cy="396" r="11" fill="none" stroke="var(--white)" stroke-width="2"/>
    <path d="M306,390 q-1,7 6,12 l2,-2.5 l-2.5,-2.5 l-1.5,1 q-2.5,-2 -3,-4.5 l1.5,-1 l-1,-3.5 Z" fill="var(--white)"/>
    <text class="phone" x="333" y="408">860.417.2938</text>
    <text class="cta-sub" x="336" y="428">FOR A FREE ESTIMATE</text>

    <!-- social -->
    <text class="follow" x="569" y="395">Follow Us On</text>
    <g fill="var(--ink)">
      <circle cx="575" cy="414" r="8.5"/><circle cx="597" cy="414" r="8.5"/>
      <circle cx="620" cy="414" r="8.5"/><circle cx="643" cy="414" r="8.5"/>
      <circle cx="665" cy="414" r="8.5"/>
    </g>
  </svg>

  <!-- Back side -->
  <svg class="postcard postcard--back" viewBox="0 0 703 454" xmlns="http://www.w3.org/2000/svg" aria-label="Postcard back">
    <defs>
      <linearGradient id="backdropPhoto" x1="0" y1="0" x2="1" y2="1">
        <stop offset="0" stop-color="#3a3a3c"/><stop offset=".6" stop-color="#2b2b2d"/><stop offset="1" stop-color="#232325"/>
      </linearGradient>
    </defs>
    <rect width="703" height="454" fill="var(--paper)"/>

    <path role="img" aria-label="Faded aerial photo of an office park parking lot" d="M0,0 H703 V150 C600,120 450,160 350,230 C250,300 110,292 0,250 Z" fill="url(#backdropPhoto)"/>
    <path d="M703,150 C600,120 450,160 350,230 C250,300 110,292 0,250 V262 C110,308 258,314 356,250 C456,184 600,168 703,222 Z" fill="var(--red)"/>

    <path d="M0,28 H122 A12,12 0 0 1 122,52 H0" fill="none" stroke="var(--white)" stroke-width="1.5"/>
    <text class="pill-label pill-label--back" x="22" y="45">About Us</text>

    <text class="about" x="22" y="72" textLength="660" lengthAdjust="spacing">BrinWeld Pavement Services is a professional, family-run company proud of it's experience servicing commercial pavements since</text>
    <text class="about" x="22" y="85" textLength="660" lengthAdjust="spacing">1994 when brothers Owen &amp; Curtis teamed up to create 'The Halbrook Company'. Today, with support from a staff of dedicated</text>
    <text class="about" x="22" y="98" textLength="660" lengthAdjust="spacing">employees BrinWeld has become a market leader in commercial pavement applications and has even been recognized as a Top 50</text>
    <text class="about" x="22" y="111">Contractor nationally by Surface Upkeep &amp; Reconstruction Journal.</text>

    <text class="cta-back" x="22" y="167">CALL FOR A FREE ESTIMATE</text>
    <circle cx="35" cy="200" r="12" fill="none" stroke="var(--white)" stroke-width="2"/>
    <path d="M29.5,193.5 q-1,8 6.5,13 l2,-2.7 l-2.7,-2.7 l-1.6,1.1 q-2.7,-2.2 -3.2,-4.9 l1.6,-1.1 l-1.1,-3.8 Z" fill="var(--white)"/>
    <text class="phone phone--back" x="58" y="213">860.417.2938</text>

    <circle cx="46" cy="346" r="9" fill="var(--red)"/>
    <text class="brand-name" x="61" y="356">brinweld</text>
    <text class="brand-tagline" x="44" y="372">PAVEMENT SERVICES</text>

    <rect x="602" y="235" width="60" height="63" fill="none" stroke="#555" stroke-width="1"/>
    <line x1="340" y1="333" x2="662" y2="333" stroke="var(--line)" stroke-width="1"/>
    <line x1="340" y1="371" x2="662" y2="371" stroke="var(--line)" stroke-width="1"/>
    <line x1="340" y1="405" x2="662" y2="405" stroke="var(--line)" stroke-width="1"/>
  </svg>

</main>
</body>
</html>
```